KORBALT

The business want a professional looking business card. We have a scetch we will add but want the extra upgrade, and would like more suggestions for variations of our business cards.

```html
<!DOCTYPE html>
<html lang="en">
<head>
<meta charset="utf-8">
<title>KORBALT business card</title>
<link rel="stylesheet" href="https://fonts.googleapis.com/css2?family=Playfair+Display:wght@600&family=Outfit:wght@300;400&display=swap">
<style>
  :root {
    --backdrop: #cbc7c2;
    --card: #f6f3ee;
    --ink: #33362f;
    --ink-soft: #4a4d46;
    --gold: #a38c5a;
    --muted: #b3aea8;
    --label: #4c4c4a;
  }
  * { margin: 0; padding: 0; box-sizing: border-box; }
  html, body {
    width: 1200px; height: 702px; overflow: hidden;
    background: var(--backdrop);
  }
  .canvas { position: relative; width: 1200px; height: 702px; }
  .side-label {
    position: absolute; left: 171px;
    font-family: "Outfit", sans-serif; font-weight: 400;
    font-size: 26px; letter-spacing: 1px; color: var(--label);
  }
  .side-label--front { top: 176px; }
  .side-label--back { top: 498px; }
  .card {
    position: absolute; left: 343px; width: 532px; height: 296px;
    background: var(--card);
  }
  .card--front { top: 40px; }
  .card--back { top: 367px; }

  .holder-name {
    position: absolute; left: 31px; top: 42px;
    font-family: "Playfair Display", serif; font-weight: 600;
    font-size: 33px; color: var(--ink); letter-spacing: -0.3px;
  }
  .holder-role {
    position: absolute; left: 31px; top: 88px;
    font-family: "Outfit", sans-serif; font-weight: 400;
    font-size: 24px; color: var(--ink);
  }
  .contact-list {
    position: absolute; left: 31px; top: 170px; list-style: none;
    font-family: "Outfit", sans-serif; font-weight: 400;
    font-size: 21px; color: var(--ink);
  }
  .contact-item { display: flex; align-items: center; height: 33.5px; }
  .contact-icon { width: 15px; margin-right: 0; color: var(--ink-soft); }

  .brand-mark { position: absolute; }
  .brand-mark--front { right: 20px; top: 150px; width: 160px; text-align: center; }
  .brand-dot { display: block; border-radius: 50%; background: var(--gold); }
  .brand-mark--front .brand-dot { width: 58px; height: 58px; margin: 0 auto 24px; }
  .brand-name {
    font-family: "Playfair Display", serif; font-weight: 600;
    color: var(--ink); letter-spacing: 6px;
  }
  .brand-mark--front .brand-name { font-size: 22px; }

  .brand-mark--back {
    left: 78px; top: 142px; display: flex; align-items: center;
  }
  .brand-mark--back .brand-dot { width: 76px; height: 76px; margin-right: 19px; }
  .brand-lockup { display: flex; flex-direction: column; }
  .brand-since {
    font-family: "Outfit", sans-serif; font-weight: 300;
    font-size: 19px; letter-spacing: 13px; color: var(--muted);
    margin-bottom: 6px;
  }
  .brand-mark--back .brand-name { font-size: 34px; letter-spacing: 10px; }
</style>
</head>
<body>
<main class="canvas">
  <span class="side-label side-label--front">FRONT</span>
  <span class="side-label side-label--back">BACK</span>

  <section class="card card--front" aria-label="Card front">
    <h1 class="holder-name">Lars Erik Solvang</h1>
    <p class="holder-role">CEO &amp; Founder</p>
    <ul class="contact-list">
      <li class="contact-item">
        <svg class="contact-icon" viewBox="0 0 15 15" aria-hidden="true"><circle cx="4" cy="7.5" r="3" fill="currentColor"/></svg>
        <span>004791234567</span>
      </li>
      <li class="contact-item">
        <svg class="contact-icon" viewBox="0 0 15 15" aria-hidden="true"><path d="M2.5 3.5 L6 7.5 L2.5 11.5" fill="none" stroke="currentColor" stroke-width="2" stroke-linecap="round"/></svg>
        <span>post@korbalt.llc</span>
      </li>
      <li class="contact-item">
        <svg class="contact-icon" viewBox="0 0 15 15" aria-hidden="true"><circle cx="4" cy="7.5" r="2" fill="currentColor"/></svg>
        <span>www.korbalt.llc</span>
      </li>
    </ul>
    <div class="brand-mark brand-mark--front">
      <span class="brand-dot" aria-hidden="true"></span>
      <span class="brand-name">KORBALT</span>
    </div>
  </section>

  <section class="card card--back" aria-label="Card back">
    <div class="brand-mark brand-mark--back">
      <span class="brand-dot" aria-hidden="true"></span>
      <div class="brand-lockup">
        <span class="brand-since">SINCE 2026</span>
        <span class="brand-name">KORBALT</span>
      </div>
    </div>
  </section>
</main>
</body>
</html>
```